Smart Design for Global Industrial Business

We are commissioned to replace an existing industrial business website with a new website with new branding and layout for CMS / Responsive (Wordpress). The existing website is to be replaced (vortanfixings.com) with one that is more in keeping with the new brand book and modern design standards.
Note that they have two online stores (vtn-gripping.co.uk and .com) and this site will need to fit with those, whilst being very different and much more about VTN and their scope / reach.
Please just design the homepage first as we will try to give everyone a chance to build from there if they are heading in the right direction.
The eventual delivery will be of all the wireframes, in source file format (ideally PSD) as well as PNGs.
We will aim to feedback in detail to all participants, but if you really don't try that hard, it may be brief!

Target Market(s)

Buyers in companies who are looking for clamping / restraining products - to persuade them that these are the best, most reliable, products.

Industry/Entity Type

Industrial safety/banding products

Number of Pages Required

5+ page

Font styles to use
Sans Serif
Other font styles liked:
• see current websites

Requirements
Must have
• A really good consistent level of design with consideration of mobile users and lead generation.
Nice to have
• I just want to see good creative, if possible. Don't try too many things, keep it simple.
Should not have
• No untidiness or lack of consistency.

```html
<!DOCTYPE html>
<html lang="en">
<head>
<meta charset="utf-8">
<title>VTN – Homepage design board</title>
<link href="https://fonts.googleapis.com/css2?family=Barlow:wght@400;500;600;700&family=Roboto:wght@400;500&display=swap" rel="stylesheet">
<style>
:root{
  --navy:#334353;
  --orange:#ff6129;
  --light:#f9f9f9;
  --board:#fde3da;
  --grey-bg:#f3f3f3;
  --text:#4a5561;
  --muted:#8a939c;
  --photo-dark:linear-gradient(160deg,#4b525a 0%,#6b6f71 45%,#2d3238 100%);
  --photo-sea:linear-gradient(180deg,#aeb8bf 0%,#7f8d93 55%,#8d8676 100%);
  --photo-beach:linear-gradient(180deg,#9fb2c2 0%,#6f9fb0 50%,#4d5a66 100%);
  --photo-pipe:linear-gradient(180deg,#4d6078 0%,#1f2a38 70%,#6b7c8c 100%);
  --photo-prod:linear-gradient(135deg,#f2f2f2 0%,#bdbdbd 60%,#3a3a3a 100%);
}
*{box-sizing:border-box;margin:0;padding:0}
html,body{width:1200px;height:3482px;overflow:hidden}
body{background:var(--board);font-family:"Roboto",sans-serif;color:var(--text);position:relative}
.abs{position:absolute}
.wordmark{font-family:"Barlow",sans-serif;font-weight:700;display:flex;align-items:center;gap:6px;letter-spacing:1px}
.wordmark .dot{border-radius:50%;background:currentColor;display:inline-block}

.board-logo{left:0;width:1200px;top:112px;justify-content:center;color:var(--navy);font-size:58px}
.board-logo .dot{width:18px;height:18px;background:var(--orange)}
.fonts-label,.colors-label{font-family:"Barlow",sans-serif;font-weight:600;font-size:24px;color:var(--navy)}
.fonts-label{left:322px;top:280px}
.font-main{left:405px;top:270px;font-family:"Barlow",sans-serif;font-size:24px;color:var(--navy);letter-spacing:.5px}
.font-sub{left:405px;top:303px;font-size:15px;color:var(--navy)}
.colors-label{left:718px;top:282px}
.swatch{top:266px;width:44px;height:44px;border-radius:50%}
.swatch-label{top:320px;font-size:11px;color:var(--muted);width:60px;text-align:center}

.screen{overflow:hidden;background:var(--navy)}
.screen .bar{background:var(--orange);height:4%}
.screen .hero{position:absolute;left:0;right:0;bottom:0;background:var(--photo-dark);display:flex;flex-direction:column;align-items:center;justify-content:center;text-align:center;color:#fff;font-family:"Barlow",sans-serif;font-weight:600;text-transform:uppercase}
.screen .brand{color:#fff;position:absolute}
.screen .kicker{color:var(--orange);letter-spacing:3px;font-weight:500}

.side-caption{font-family:"Barlow",sans-serif;font-size:17px;letter-spacing:9px;color:var(--navy);transform:rotate(-90deg);transform-origin:left top;white-space:nowrap}

.page{position:absolute;background:#fff;overflow:hidden}
.page-desktop{left:161px;top:983px;width:598px;height:2400px}
.page-desktop .topbar{left:0;top:0;width:598px;height:16px;background:var(--orange);color:#fff;font-size:5px;display:flex;align-items:center;justify-content:space-between;padding:0 81px}
.page-desktop .nav{left:0;top:16px;width:598px;height:60px;background:var(--navy);display:flex;align-items:center;padding:0 81px}
.page-desktop .nav .wordmark{color:#fff;font-size:26px}
.page-desktop .nav .wordmark .dot{width:8px;height:8px}
.nav-links{display:flex;gap:13px;margin-left:60px;font-family:"Barlow",sans-serif;font-weight:500;font-size:6px;color:#fff;text-transform:uppercase}
.d-hero{left:0;top:76px;width:598px;height:370px;background:var(--photo-dark)}
.d-hero .kicker{position:absolute;top:100px;width:100%;text-align:center;font-family:"Barlow",sans-serif;font-size:8px;letter-spacing:6px;color:var(--orange)}
.d-hero h1{position:absolute;top:118px;width:100%;text-align:center;font-family:"Barlow",sans-serif;font-weight:600;font-size:26px;line-height:32px;color:#fff;text-transform:uppercase}
.arrow-btn{position:absolute;width:23px;height:23px;display:flex;align-items:center;justify-content:center}
.d-cards{left:81px;top:390px;width:437px;height:108px;background:#fff;box-shadow:0 2px 8px rgba(0,0,0,.12);display:flex;padding:4px;gap:5px}
.card{flex:1;position:relative;padding:36px 0 0 12px;font-family:"Barlow",sans-serif;font-weight:500;font-size:9px;line-height:11px;text-transform:uppercase;color:var(--navy)}
.card.active{background:var(--navy);color:#fff}
.card .rule{width:18px;height:2px;background:var(--orange);margin-top:8px}
.card .prod{position:absolute;right:8px;top:22px;width:56px;height:52px;border-radius:6px;background:var(--photo-prod)}
.copy{font-size:5px;line-height:9px;color:var(--text)}
.copy p+p{margin-top:9px}
.copy a{color:var(--orange);text-decoration:underline}
.h2{font-family:"Barlow",sans-serif;font-weight:600;font-size:16px;line-height:19px;color:var(--navy);text-transform:uppercase}
.h2c{text-align:center;left:0;width:598px}
.rule-o{height:2px;width:22px;background:var(--orange)}
.photo{border:1px solid #ddd}
.select{border:1px solid #bbb;font-size:5px;display:flex;align-items:center;justify-content:space-between;padding:0 8px;color:var(--navy)}
.btn{background:var(--orange);color:#fff;font-family:"Barlow",sans-serif;font-weight:600;font-size:5px;display:flex;align-items:center;justify-content:center;text-transform:uppercase}
.grey{background:var(--grey-bg)}
.case{height:124px}
.case .cap{position:absolute;left:0;right:0;bottom:0;height:22px;background:var(--navy);color:#fff;font-size:5px;line-height:6px;padding:5px 8px;display:flex;justify-content:space-between}
.case .cap.o{background:var(--orange)}
.news-item{width:102px}
.news-item .img{height:81px}
.news-item .meta{font-size:4px;color:var(--muted);margin-top:10px}
.news-item .title{font-size:6px;line-height:9px;color:var(--navy);margin-top:5px}
.contact-h{font-family:"Barlow",sans-serif;font-weight:500;font-size:15px;line-height:19px;color:var(--navy)}
.row{display:flex;font-size:5px;line-height:8px}
.row b{width:50px;font-weight:500;color:var(--navy)}
.footer{left:0;top:2102px;width:598px;height:298px;background:var(--navy);color:#fff}
.fcol{position:absolute;top:36px}
.fcol h4{font-family:"Barlow",sans-serif;font-weight:600;font-size:9px;margin-bottom:18px}
.fcol li{list-style:none;font-size:5px;line-height:18px;color:#d5dbe1}
.fcol li.u{text-decoration:underline}
.social{display:flex;gap:4px;margin-top:6px}
.social span{width:10px;height:10px;background:#fff}
.social span:nth-child(2){background:var(--orange)}
.fbottom{position:absolute;top:264px;left:81px;right:81px;font-size:4px;color:#c8d0d8;display:flex;justify-content:space-between}

.page-mobile{left:906px;top:983px;width:104px;height:2400px}
.m{position:absolute;left:7px;width:90px}
.m-card{left:7px;width:90px;height:58px;background:#fff;box-shadow:0 1px 4px rgba(0,0,0,.12);font-family:"Barlow",sans-serif;font-size:6px;line-height:7px;color:var(--navy);padding:22px 0 0 8px;text-transform:uppercase}
.m-card.active{background:var(--navy);color:#fff}
.m-card .prod{position:absolute;right:6px;top:14px;width:30px;height:30px;border-radius:4px;background:var(--photo-prod)}
.mt{font-size:2.6px;line-height:4.4px;color:var(--text)}
.mh{font-family:"Barlow",sans-serif;font-weight:600;font-size:7px;line-height:8px;color:var(--navy);text-transform:uppercase}
</style>
</head>
<body>

<div class="abs wordmark board-logo"><span class="dot"></span>VTN</div>
<div class="abs fonts-label">Fonts:</div>
<div class="abs font-main">BARLOW</div>
<div class="abs font-sub">Roboto</div>
<div class="abs colors-label">Colors:</div>
<div class="abs swatch" style="left:808px;background:#334353"></div>
<div class="abs swatch" style="left:864px;background:#ff6129"></div>
<div class="abs swatch" style="left:920px;background:#f9f9f9"></div>
<div class="abs swatch-label" style="left:800px">#334353</div>
<div class="abs swatch-label" style="left:856px">#ff6129</div>
<div class="abs swatch-label" style="left:912px">#f9f9f9</div>

<div class="abs screen" style="left:354px;top:432px;width:584px;height:324px">
  <div class="bar"></div>
  <div class="brand wordmark" style="left:80px;top:24px;font-size:20px">VTN</div>
  <div class="hero" style="top:68px" role="img" aria-label="Hero photo: pier on dark pilings over a rocky shore">
    <div class="kicker" style="font-size:7px">Welcome to VTN</div>
    <div style="font-size:25px;line-height:31px;margin-top:6px">The leading manufacturer<br>and supplier of clamping<br>and banding solutions</div>
  </div>
</div>
<div class="abs screen" style="left:161px;top:672px;width:364px;height:230px">
  <div class="bar"></div>
  <div class="brand wordmark" style="left:50px;top:14px;font-size:13px">VTN</div>
  <div class="hero" style="top:40px" role="img" aria-label="Hero photo: pier on dark pilings over a rocky shore">
    <div class="kicker" style="font-size:5px">Welcome to VTN</div>
    <div style="font-size:15px;line-height:19px;margin-top:4px">The leading manufacturer<br>and supplier of clamping<br>and banding solutions</div>
  </div>
</div>
<div class="abs screen" style="left:902px;top:686px;width:104px;height:232px">
  <div class="bar"></div>
  <div class="brand wordmark" style="left:8px;top:14px;font-size:10px">VTN</div>
  <div class="hero" style="top:38px;bottom:30px" role="img" aria-label="Hero photo: pier on dark pilings over a rocky shore">
    <div class="kicker" style="font-size:4px">Welcome to VTN</div>
    <div style="font-size:9px;line-height:14px;margin-top:4px">The leading<br>manufacturer<br>and supplier of<br>clamping and<br>banding solutions</div>
  </div>
  <div class="abs" style="left:0;right:0;bottom:0;height:30px;background:#fff;font-family:Barlow,sans-serif;font-size:6px;color:var(--navy);padding:18px 0 0 8px">HOSE</div>
</div>

<div class="abs side-caption" style="left:118px;top:2372px">LAPTOP / DESKTOP</div>
<div class="abs side-caption" style="left:881px;top:2290px">RESPONSIVE</div>

<div class="page page-desktop">
  <div class="abs topbar"><span>☎ +44 (0) 1632 960 214 &nbsp; | &nbsp; ☎ +1 555 010 0143</span><span>News &nbsp;|&nbsp; About Us &nbsp;|&nbsp; Contact Us</span></div>
  <div class="abs nav">
    <div class="wordmark"><span class="dot"></span>VTN</div>
    <div class="nav-links"><span>Hose Clamps</span><span>Banding &amp; Saddles</span><span>Custom Solutions</span><span>Applications</span><span>Case Studies</span></div>
  </div>
  <div class="abs d-hero" role="img" aria-label="Hero photo: pier on dark pilings over a rocky shore under a grey sky">
    <div class="kicker">WELCOME TO VTN</div>
    <h1>The leading manufacturer<br>and supplier of clamping<br>and banding solutions</h1>
    <div class="arrow-btn" style="left:52px;top:145px;background:rgba(255,255,255,.15)"><svg width="8" height="8" viewBox="0 0 8 8"><path d="M7 4H1M3.5 1.5 1 4l2.5 2.5" stroke="#fff" fill="none"/></svg></div>
    <div class="arrow-btn" style="left:522px;top:145px;background:var(--orange)"><svg width="8" height="8" viewBox="0 0 8 8"><path d="M1 4h6M4.5 1.5 7 4 4.5 6.5" stroke="#fff" fill="none"/></svg></div>
  </div>
  <div class="abs d-cards">
    <div class="card">Hose<br>Clamps<div class="rule"></div><div class="prod" role="img" aria-label="Product photo: black hose clamps"></div></div>
    <div class="card active">Banding<br>Solutions<div class="rule"></div><div class="prod" role="img" aria-label="Product photo: banding tool"></div></div>
    <div class="card">Custom<br>Solutions<div class="rule"></div><div class="prod" role="img" aria-label="Product photo: custom clamping tools"></div></div>
  </div>

  <div class="abs copy" style="left:81px;top:538px;width:205px">
    <p>VTN is one of the world's leading producers and suppliers of clamping systems for commercial &amp; personal use. We manufacture non-metallic smart polymer hose clamps &amp; clips - including <a>Spiralok Clip</a>, <a>Snapgrip</a> and range of <a>tools</a>.</p>
    <p>We also supply a wide range of <a>selected high quality distributed brands</a> from the most recognized and respected brands of hose clamps and clips.</p>
  </div>
  <div class="abs copy" style="left:309px;top:538px;width:209px">
    <p>With warehouses in the US and the UK we are now supplying across the world both standard and <a>custom solutions</a> to deliver long-lasting, reliable and secure clamping and banding solutions.</p>
    <p>So, please browse our website or <a>contact us</a> if you have a specific requirement, we look forward to hearing from you.</p>
  </div>

  <div class="abs h2" style="left:81px;top:683px;width:200px">Water. Sun. Cold. Salt. Wind... We've got it covered</div>
  <div class="abs rule-o" style="left:81px;top:752px"></div>
  <div class="abs copy" style="left:81px;top:770px;width:205px">
    <p>There are many situations where you need the right solution to make sure that whatever you need to secure is fixed for good.</p>
    <p>At VTN, our aim is to recommend the best product for your specific situation, regardless of whether it is ours, or from another company.</p>
    <p>So select your challenge, and explore the best product(s) to suit your needs.</p>
  </div>
  <div class="abs select" style="left:81px;top:855px;width:138px;height:25px"><span>CHOOSE A CHALLENGE</span><span>⌄</span></div>
  <div class="abs photo" style="left:310px;top:686px;width:207px;height:190px;background:var(--photo-sea)" role="img" aria-label="Photo: floating pipeline laid across a tidal shore"></div>

  <div class="abs grey" style="left:0;top:920px;width:598px;height:267px"></div>
  <div class="abs photo" style="left:81px;top:957px;width:205px;height:195px;background:var(--photo-beach)" role="img" aria-label="Photo: long jetty on piles over turquoise water"></div>
  <div class="abs h2" style="left:310px;top:958px">Custom Solutions</div>
  <div class="abs copy" style="left:310px;top:1000px;width:208px"><p>Our specialization is non-metallic polymer hose clamps, clips and banding means that we supply to specific projects around the world. Discover how we may be able to assist you.</p></div>
  <div class="abs btn" style="left:310px;top:1048px;width:73px;height:23px">Find out more</div>
  <div class="abs copy" style="left:310px;top:1085px;width:208px">
    <p>Or, if you prefer, <a>contact our sales team</a></p>
    <p>They are experienced in helping understand your requirements, and will bring together a full proposal for exactly what you need. This may include any specialist tools and recommendations on installation partners needed to fulfil the project.</p>
  </div>

  <div class="abs h2 h2c" style="top:1232px">Case Studies - VTN Products in Place</div>
  <div class="abs rule-o" style="left:288px;top:1256px"></div>
  <div class="abs case" style="left:81px;top:1277px;width:138px;background:var(--photo-pipe)" role="img" aria-label="Photo: pile wrap system on a dark marine pile"><div class="cap"><span>Pile Wrap System -<br>Northcliff</span><span>→</span></div></div>
  <div class="abs case" style="left:230px;top:1277px;width:138px;background:linear-gradient(180deg,#3c6ea8,#5d7390 60%,#8a8f8a)" role="img" aria-label="Photo: engineers on a lift beside a harbour pile"><div class="cap o"><span>ICCP - Greyhaven</span><span>→</span></div></div>
  <div class="abs case" style="left:379px;top:1277px;width:139px;background:linear-gradient(180deg,#7a8188,#3b4147 60%,#6d6a60)" role="img" aria-label="Photo: subsea cable with attachments on a vessel deck"><div class="cap"><span>Subsea Cable<br>Attachment - Westmoor</span><span>→</span></div></div>

  <div class="abs grey" style="left:0;top:1430px;width:598px;height:320px"></div>
  <div class="abs h2 h2c" style="top:1481px">News, Events &amp; Features</div>
  <div class="abs rule-o" style="left:288px;top:1505px"></div>
  <div class="abs news-item" style="left:81px;top:1527px"><div class="img" style="background:linear-gradient(180deg,#2f4f86,#4a6aa0 60%,#c9ccd0)" role="img" aria-label="Photo: exhibition stand at a trade conference"></div><div class="meta">BY ADMIN | SEP 8, 2021</div><div class="title">We attended the Maritime 2021 conference</div></div>
  <div class="abs news-item" style="left:193px;top:1527px"><div class="img" style="background:linear-gradient(180deg,#d0d3d6,#b84a2a 60%,#5a4a40)" role="img" aria-label="Photo: technician in orange overalls at an installation"></div><div class="meta">BY ADMIN | SEP 8, 2021</div><div class="title">A video of a recent installation in Saudi Arabia</div></div>
  <div class="abs news-item" style="left:305px;top:1527px"><div class="img" style="background:linear-gradient(180deg,#5d6a74,#20262c 60%,#6a7178)" role="img" aria-label="Photo: product testing on a workshop floor"></div><div class="meta">BY ADMIN | SEP 8, 2021</div><div class="title">Testing our products, how we make sure that VTN solutions are fit for purpose</div></div>
  <div class="abs news-item" style="left:416px;top:1527px"><div class="img" style="background:var(--photo-prod)" role="img" aria-label="Photo: clamping tools on a white background"></div><div class="meta">BY ADMIN | SEP 8, 2021</div><div class="title">Custom tools - when you need to make sure the fit is right</div></div>
  <div class="abs btn" style="left:264px;top:1697px;width:71px;height:25px">Read more news</div>

  <div class="abs contact-h" style="left:81px;top:1793px">VTN FIXINGS LIMITED for<br>UK, EU, EMEA &amp; Worldwide</div>
  <div class="abs rule-o" style="left:81px;top:1840px"></div>
  <div class="abs row" style="left:81px;top:1858px"><b>Main Office:</b><span>Unit 4, Marlow Trade Park, Norbury,<br>Wessex BA0 1XX - United Kingdom</span></div>
  <div class="abs row" style="left:81px;top:1885px"><b>Telephone:</b><span>+44 (0) 1632 960 214</span></div>
  <div class="abs contact-h" style="left:81px;top:1923px">VTN FIXINGS CORP for<br>USA &amp; Canada</div>
  <div class="abs rule-o" style="left:81px;top:1970px"></div>
  <div class="abs row" style="left:81px;top:1988px"><b>Main Office:</b><span>Suite 12, 4400 Ridgeway Drive,<br>Lakeview, Texas 77000 - United States</span></div>
  <div class="abs row" style="left:81px;top:2015px"><b>Telephone:</b><span>+1 555 010 0143</span></div>
  <div class="abs btn" style="left:81px;top:2052px;width:72px;height:25px">Contact us now</div>
  <div class="abs photo" style="left:310px;top:1793px;width:208px;height:273px;background:var(--photo-pipe)" role="img" aria-label="Photo: large pipe sections with clamps on a deck">
    <div class="abs wordmark" style="left:0;right:0;bottom:0;height:36px;background:var(--navy);color:#fff;font-size:8px;justify-content:center">VTN GRIPPING LTD</div>
  </div>

  <div class="abs footer">
    <div class="fcol" style="left:81px"><h4>Hose Clamps</h4><ul><li>Spiralok Clips</li><li>Quickbind</li><li>Snapgrip</li><li>Air Tools</li><li>Distributed Brands</li></ul></div>
    <div class="fcol" style="left:198px"><h4>Banding &amp; Saddles</h4><ul><li>FlexBand</li><li>GripTie</li><li>EdgeGuard Protectors</li><li>CradleFit Saddles</li><li>Installation Tools</li></ul></div>
    <div class="fcol" style="left:340px"><h4>Discover VTN</h4><ul><li>Custom Solutions</li><li>Applications</li><li>Case Studies</li><li>Quality &amp; Testing</li><li>Facility</li><li>Contact Us</li></ul></div>
    <div class="fcol" style="left:459px"><h4>Contact VTN</h4><ul><li class="u">Send an Email</li><li>UK/EU</li><li class="u">Tel: +44 (0) 1632 960 214</li><li class="u">Online Store</li><li>USA</li><li class="u">Tel: +1 555 010 0143</li><li class="u">Toll Free: 1-800-555-0199</li><li class="u">Online Store</li></ul><div class="social"><span></span><span></span><span></span></div></div>
    <div class="fbottom"><span>© VTN Fixings Limited - All Rights Reserved</span><span>Sitemap &nbsp;|&nbsp; Terms Of Use &nbsp;|&nbsp; Privacy Policy &nbsp;|&nbsp; Contact Us</span></div>
  </div>
</div>

<div class="page page-mobile">
  <div class="abs" style="left:0;top:0;width:104px;height:11px;background:var(--orange);font-size:3px;color:#fff;padding:3px 6px">☎ +44 (0) 1632 960 214 | ☎ +1 555 010 0143</div>
  <div class="abs" style="left:0;top:11px;width:104px;height:32px;background:var(--navy)"><div class="abs wordmark" style="left:8px;top:9px;color:#fff;font-size:11px">VTN</div><div class="abs" style="right:7px;top:14px;width:8px;height:5px;border-top:1px solid #fff;border-bottom:1px solid #fff"></div></div>
  <div class="abs" style="left:0;top:43px;width:104px;height:205px;background:var(--photo-dark);text-align:center;color:#fff;font-family:Barlow,sans-serif;font-weight:600" role="img" aria-label="Hero photo: pier on dark pilings over a rocky shore">
    <div style="margin-top:18px;font-size:4px;letter-spacing:2px;color:var(--orange)">WELCOME TO VTN</div>
    <div style="font-size:8px;line-height:13px;margin-top:4px">THE LEADING<br>MANUFACTURER<br>AND SUPPLIER OF<br>CLAMPING AND<br>BANDING SOLUTIONS</div>
  </div>
  <div class="abs m-card" style="top:158px">Hose<br>Clamps<div class="prod" role="img" aria-label="Product photo: hose clamps"></div></div>
  <div class="abs m-card active" style="top:225px">Banding<br>Solutions<div class="prod" role="img" aria-label="Product photo: banding tool"></div></div>
  <div class="abs m-card" style="top:292px">Custom<br>Solutions<div class="prod" role="img" aria-label="Product photo: custom tools"></div></div>
  <div class="abs m mt" style="top:374px">VTN is one of the world's leading producers and suppliers of clamping systems for commercial &amp; personal use. We manufacture non-metallic smart polymer hose clamps &amp; clips and a range of tools. With warehouses in the US and the UK we supply across the world both standard and custom solutions. Please browse our website or contact us with a specific requirement.</div>
  <div class="abs m" style="top:517px;height:84px;background:var(--photo-sea)" role="img" aria-label="Photo: floating pipeline across a tidal shore"></div>
  <div class="abs m mh" style="top:613px">Water. Sun. Cold. Salt. Wind... We've got it covered</div>
  <div class="abs" style="left:7px;top:648px;width:12px;height:1px;background:var(--orange)"></div>
  <div class="abs m mt" style="top:660px">There are many situations where you need the right solution to make sure it is fixed for good. Our aim is to recommend the best product for your situation. Select your challenge and explore.</div>
  <div class="abs m select" style="top:729px;height:13px;font-size:3px;padding:0 4px"><span>CHOOSE A CHALLENGE</span><span>⌄</span></div>
  <div class="abs m" style="top:782px;height:88px;background:var(--photo-beach)" role="img" aria-label="Photo: jetty on piles over turquoise water"></div>
  <div class="abs m mh" style="top:885px">Custom Solutions</div>
  <div class="abs m mt" style="top:912px">Our specialization in non-metallic polymer hose clamps, clips and banding means we supply to specific projects around the world.</div>
  <div class="abs btn" style="left:7px;top:946px;width:40px;height:11px;font-size:3px">Find out more</div>
  <div class="abs m mt" style="top:965px">Or, contact our sales team. They will bring together a full proposal for exactly what you need, including tools and installation partners.</div>
  <div class="abs m mh" style="top:1028px">Case Studies -<br>VTN Products<br>in Place</div>
  <div class="abs m" style="top:1084px;height:72px;background:var(--photo-pipe)" role="img" aria-label="Photo: pile wrap system"><div class="abs" style="left:0;right:0;bottom:0;height:12px;background:var(--navy)"></div></div>
  <div class="abs m" style="top:1165px;height:72px;background:linear-gradient(180deg,#3c6ea8,#8a8f8a)" role="img" aria-label="Photo: harbour pile installation"><div class="abs" style="left:0;right:0;bottom:0;height:12px;background:var(--orange)"></div></div>
  <div class="abs m" style="top:1246px;height:72px;background:linear-gradient(180deg,#7a8188,#3b4147)" role="img" aria-label="Photo: subsea cable attachment"><div class="abs" style="left:0;right:0;bottom:0;height:12px;background:var(--navy)"></div></div>
  <div class="abs m mh" style="top:1366px">News, Events<br>&amp; Features</div>
  <div class="abs m" style="top:1406px;height:62px;background:linear-gradient(180deg,#2f4f86,#c9ccd0)" role="img" aria-label="Photo: exhibition stand"></div>
  <div class="abs m" style="top:1491px;height:62px;background:linear-gradient(180deg,#d0d3d6,#b84a2a)" role="img" aria-label="Photo: technician at installation"></div>
  <div class="abs m" style="top:1577px;height:62px;background:linear-gradient(180deg,#5d6a74,#20262c)" role="img" aria-label="Photo: product testing"></div>
  <div class="abs m" style="top:1662px;height:62px;background:var(--photo-prod)" role="img" aria-label="Photo: clamping tools"></div>
  <div class="abs btn" style="left:7px;top:1766px;width:44px;height:12px;font-size:3px">Read more news</div>
  <div class="abs m" style="top:1821px;height:113px;background:var(--photo-pipe)" role="img" aria-label="Photo: large pipe sections on a deck"><div class="abs wordmark" style="left:0;right:0;bottom:0;height:18px;background:var(--navy);color:#fff;font-size:4px;justify-content:center">VTN GRIPPING LTD</div></div>
  <div class="abs m mh" style="top:1948px;font-weight:500;text-transform:none">VTN FIXINGS LIMITED<br>UK, EU, EMEA &amp; Worldwide</div>
  <div class="abs m mt" style="top:1970px">Main Office: Unit 4, Marlow Trade Park, Norbury<br>Telephone: +44 (0) 1632 960 214</div>
  <div class="abs m mh" style="top:1988px;font-weight:500;text-transform:none">VTN FIXINGS CORP for<br>USA &amp; Canada</div>
  <div class="abs m mt" style="top:2010px">Main Office: Suite 12, 4400 Ridgeway Drive<br>Telephone: +1 555 010 0143</div>
  <div class="abs btn" style="left:7px;top:2028px;width:40px;height:10px;font-size:3px">Contact us now</div>
  <div class="abs" style="left:0;top:2051px;width:104px;height:349px;background:var(--navy);color:#fff;font-size:3px;line-height:6px;padding:14px 7px">
    <div style="display:flex;justify-content:space-between"><div><b>Hose Clamps</b><br>Spiralok Clips<br>Quickbind<br>Snapgrip<br>Air Tools<br>Distributed Brands</div><div><b>Banding &amp; Saddles</b><br>FlexBand<br>GripTie<br>EdgeGuard Protectors<br>CradleFit Saddles<br>Installation Tools</div></div>
    <div style="display:flex;justify-content:space-between;margin-top:10px"><div><b>Discover VTN</b><br>Custom Solutions<br>Applications<br>Case Studies<br>Quality &amp; Testing<br>Facility<br>Contact Us</div><div><b>Contact VTN</b><br>Send an Email<br>UK/EU<br>+44 (0) 1632 960 214<br>USA<br>+1 555 010 0143<br>Online Store</div></div>
    <div style="margin-top:40px;text-align:center;color:#c8d0d8">Sitemap | Terms | Privacy | Contact<br>© VTN Fixings Limited</div>
  </div>
</div>

</body>
</html>
```